I need a book cover (front and back) for a book I wrote called "7 Habits of Polish: A Closet Method for Confidence".

The short version of the book can be found online here: https://filevault-share.example/file/d/8KpQm3RtZx2LwYv9NcHj4BsDf7GaUoEi/view

I'm working on expanding this into a real book (100+ pages, with images), and putting it on Brindlemart.

I'm the author, Lou Markovitch. I was named "Sharpest Gent of the Nation" by Dapperline Journal, and I would like to add that to the cover for credibility.

My website "About Page" has more info about me and my business Threadwork House: https://threadworkhouse.example/pages/about-us

I also attached the first version of the cover I made using Canva.

I have LOTS of images, if you need some (mannequins, models, garments, etc). See our website's blog for more ideas of the images we have: https://threadworkhouse.example/blogs/news

```html
<!DOCTYPE html>
<html lang="en">
<head>
<meta charset="utf-8">
<title>7 Habits of Polish — Book Cover Wrap</title>
<link rel="stylesheet" href="https://fonts.googleapis.com/css2?family=Bodoni+Moda:opsz,wght@6..96,400&family=Cinzel:wght@400&family=Poppins:wght@400&display=swap">
<style>
  :root {
    --bg-warm: #4c4743;
    --bg-deep: #3e3a37;
    --suit-dark: #23222a;
    --suit-mid: #34323a;
    --cream: #fdf9d6;
    --white: #ffffff;
    --shadow: rgba(20, 18, 20, 0.85);
    --portrait-dark: #1f2630;
    --portrait-mid: #3a4350;
  }
  * { margin: 0; padding: 0; box-sizing: border-box; }
  html, body { width: 1200px; height: 873px; overflow: hidden; }
  body { background: var(--bg-deep); }

  .cover-wrap {
    position: relative;
    width: 1200px;
    height: 873px;
    overflow: hidden;
    background: linear-gradient(180deg, var(--bg-warm) 0%, var(--bg-deep) 100%);
  }

  /* Front photography area */
  .front-photo {
    position: absolute;
    left: 440px; top: 0;
    width: 760px; height: 873px;
    background:
      radial-gradient(ellipse 40% 30% at 73% 38%, rgba(225, 218, 200, 0.35), transparent 70%),
      radial-gradient(ellipse 70% 90% at 70% 55%, var(--suit-mid), transparent 75%),
      linear-gradient(90deg, transparent 0%, var(--suit-dark) 35%, var(--suit-dark) 100%);
  }

  /* Back cover */
  .author-portrait {
    position: absolute;
    left: 189px; top: 74px;
    width: 193px; height: 193px;
    background: radial-gradient(circle at 50% 45%, var(--portrait-mid), var(--portrait-dark));
  }
  .back-author {
    position: absolute;
    left: 0; top: 288px;
    width: 572px;
    text-align: center;
    font-family: "Cinzel", serif;
    font-size: 29px;
    letter-spacing: 4px;
    color: var(--white);
  }
  .back-blurb {
    position: absolute;
    left: 53px; top: 336px;
    width: 450px;
    font-family: "Poppins", sans-serif;
    font-size: 17.3px;
    line-height: 21.6px;
    color: var(--white);
  }
  .back-blurb p { text-indent: 18px; }

  /* Spine */
  .spine-text {
    position: absolute;
    writing-mode: vertical-rl;
    transform: rotate(180deg);
    white-space: nowrap;
    color: var(--white);
  }
  .spine-title {
    left: 562px; bottom: 500px;
    font-family: "Bodoni Moda", serif;
    font-size: 46px;
    line-height: 48px;
    color: var(--cream);
  }
  .spine-subtitle {
    left: 612px; bottom: 483px;
    font-family: "Poppins", sans-serif;
    font-size: 19px;
    line-height: 22px;
  }
  .spine-author {
    left: 588px; bottom: 77px;
    font-family: "Cinzel", serif;
    font-size: 25px;
    line-height: 28px;
    letter-spacing: 3.5px;
  }

  /* Front cover */
  .front-title {
    position: absolute;
    font-family: "Bodoni Moda", serif;
    font-weight: 400;
    color: var(--cream);
    text-shadow: 3px 2px 0 var(--shadow);
    white-space: nowrap;
  }
  .title-number { left: 706px; top: 160px; font-size: 236px; line-height: 236px; }
  .title-word   { left: 850px; top: 272px; font-size: 104px; line-height: 104px; }
  .title-line   { left: 770px; top: 372px; font-size: 104px; line-height: 104px; }
  .front-subtitle {
    position: absolute;
    left: 712px; top: 500px;
    font-family: "Poppins", sans-serif;
    font-size: 25px;
    color: var(--white);
    white-space: nowrap;
  }
  .front-author {
    position: absolute;
    left: 786px; top: 800px;
    font-family: "Cinzel", serif;
    font-size: 29px;
    letter-spacing: 4px;
    color: var(--white);
    white-space: nowrap;
  }
</style>
</head>
<body>
<main class="cover-wrap">
  <div class="front-photo" role="img" aria-label="Photo of a man in a dark suit, white shirt and loosened red bow tie, adjusting his cuff"></div>

  <section class="back-cover">
    <div class="author-portrait" role="img" aria-label="Author portrait in a pinstripe suit against a dark backdrop"></div>
    <h2 class="back-author">LOU MARKOVITCH</h2>
    <div class="back-blurb">
      <p>Lorem ipsum dolor sit amet, consectetur adipiscing elit, sed do eiusmod tempor incididunt ut labore et dolore magna aliqua. Quis ipsum suspendisse ultrices gravida. Risus commodo viverra maecenas accumsan lacus vel facilisis. Lorem ipsum dolor sit amet, consectetur adipiscing elit, sed do eiusmod tempor incididunt ut labore et dolore magna aliqua.</p>
      <p>Quis ipsum suspendisse ultrices gravida. Risus commodo viverra maecenas accumsan lacus vel facilisis.</p>
      <p>Risus commodo viverra maecenas accumsan lacus vel facilisis. Lorem ipsum dolor sit amet, consectetur adipiscing elit, sed do eiusmod tempor incididunt ut labore et dolore magna aliqua.</p>
    </div>
  </section>

  <section class="spine">
    <div class="spine-text spine-title">7 habits of polish</div>
    <div class="spine-text spine-subtitle">A closet method for confidence</div>
    <div class="spine-text spine-author">LOU MARKOVITCH</div>
  </section>

  <section class="front-cover">
    <h1>
      <span class="front-title title-number">7</span>
      <span class="front-title title-word">habits</span>
      <span class="front-title title-line">of polish</span>
    </h1>
    <p class="front-subtitle">A closet method for confidence</p>
    <p class="front-author">LOU MARKOVITCH</p>
  </section>
</main>
</body>
</html>
```